2 Page Business Flyer for Finance Business

Need a two page flyer created for a finance business. Lots of text and needs to fit on two pages.

Corporate business/banking look and feel. Not too many large images. Lots of white space, clean design. Attached is color palette and the text contents of the flyer.

```html
<!DOCTYPE html>
<html lang="en">
<head>
<meta charset="utf-8">
<title>Vanilla Contracts – Two Page Flyer</title>
<link href="https://fonts.googleapis.com/css2?family=Titillium+Web:wght@400;600;700&family=Open+Sans:wght@400;600&display=swap" rel="stylesheet">
<style>
  :root{
    --canvas:#e4e5ea;
    --page:#ffffff;
    --purple:#5a56a4;
    --purple-soft:#e7e5f2;
    --navy:#1b1d45;
    --wedge:#5b58a8;
    --teal:#3db59c;
    --ink:#3a3a44;
    --red:#d0433b;
    --rule:#9a98c4;
  }
  *{box-sizing:border-box;margin:0;padding:0}
  html,body{width:1200px;height:848px;overflow:hidden;background:var(--canvas)}
  body{position:relative;font-family:"Open Sans",Arial,sans-serif;color:var(--ink)}
  .page{position:absolute;top:80px;width:535px;height:692px;background:var(--page);box-shadow:4px 5px 10px rgba(0,0,0,.25);overflow:hidden}
  .page--one{left:48px}
  .page--two{left:608px}
  .hero{position:absolute;left:0;top:0;width:100%}
  .page--one .hero{height:235px;background:linear-gradient(180deg,#4a6a90 0%,#8fb4cf 45%,#d6e6f0 75%,#ffffff 100%)}
  .page--two .hero{height:215px;background:linear-gradient(180deg,#d7dde3 0%,#eef2f6 40%,#cfe3ef 75%,#ffffff 100%)}
  .content{position:absolute;left:56px;right:56px;font-size:6.4px;line-height:1.5}
  .title{position:absolute;left:0;right:0;top:170px;text-align:center;font-family:"Titillium Web",Arial,sans-serif;font-weight:600;font-size:27px;line-height:1.1;color:var(--purple)}
  .title-rule{position:absolute;left:56px;right:56px;top:235px;border-top:1px dotted var(--rule)}
  p{margin-bottom:7px;text-align:justify}
  ul{margin:0 0 8px 12px}
  li{margin-bottom:3px}
  .section-head{font-family:"Titillium Web",Arial,sans-serif;font-weight:600;font-size:11px;color:var(--purple);border-bottom:1px dotted var(--rule);padding-bottom:1px;margin:10px 0 6px}
  .outcome{display:flex;gap:10px;align-items:flex-start}
  .outcome svg{flex:0 0 24px;margin-top:2px}
  .outcome p{margin:0}
  .footer{position:absolute;left:0;bottom:0;width:535px;height:70px}
  .footer-label{position:absolute;right:18px;bottom:13px;font-size:5.5px;letter-spacing:.4px;color:#ffffff}
  .features{position:absolute;top:202px;left:60px;right:40px;display:flex;gap:8px}
  .feature{background:var(--purple-soft);padding:7px 8px 8px;font-size:6.1px;line-height:1.45}
  .feature h3{font-family:"Titillium Web",Arial,sans-serif;font-weight:600;font-size:11px;color:var(--purple);text-align:center;margin-bottom:3px}
  .feature ul{margin:0 0 0 9px}
  .feature li{margin-bottom:4px}
  .feature--traits{width:132px;height:158px}
  .feature--gains{width:155px;height:158px}
  .feature--risks{width:133px;height:158px}
  .page--two .content{top:370px;font-size:6.2px}
  .page--two p{margin-bottom:5px}
  .page--two ul{list-style:square}
</style>
</head>
<body>

<section class="page page--one">
  <div class="hero" role="img" aria-label="Photo of a businessperson with a tablet behind rising financial bar and line charts"></div>
  <h1 class="title">How does a Vanilla Option<br>contract work?</h1>
  <div class="title-rule"></div>

  <div class="content" style="top:245px">
    <p>The buyer of a vanilla option receives protection against an adverse movement in the exchange rate while allowing full participation in a beneficial move. At no time is the buyer of a Vanilla Option obligated to exercise the Option and transact the currencies, therefore providing flexibility in cases where the requirement to purchase foreign currency is not certain.</p>
    <p>A buyer of vanilla options is required to pay a premium (like an insurance premium) for the right, but not the obligation, to exchange currency at a predetermined rate on a predetermined date.</p>
    <ul>
      <li>Set a protection rate which will be your worst-case scenario at expiry</li>
      <li>Determine the amount of currency you wish to protect</li>
      <li>Choose an expiry date for the contract</li>
      <li>Calculate the premium you are required to pay</li>
    </ul>

    <h2 class="section-head">Let’s look at an example: You are in importer.</h2>
    <p>Your construction company has bid on a project that if successful, will require you to import materials from the United States to use in construction. You have used todays pricing of materials in calculating your bid and want to protect against an adverse move in the US dollar exchange rate from eroding your margin if your bid is chosen for the project.</p>
    <p>You choose to buy a Vanilla Call which will protect you from a rise in the USD/CAD exchange rate above your protection rate. You choose to buy protection on $500,000 USD, with a protection rate (strike rate) of 1.3300 expiring 3 months from now. You are required to pay a premium which in this case is calculated to be 1.8%, or 11,970 CAD.</p>

    <h2 class="section-head">Your bid is successful:</h2>
    <div class="outcome">
      <svg width="24" height="24" viewBox="0 0 24 24" aria-hidden="true">
        <circle cx="11" cy="13" r="9.5" fill="none" stroke="var(--purple)" stroke-width="1.8"/>
        <path d="M6 12.5l4.5 4.5L22 3" fill="none" stroke="var(--purple)" stroke-width="2.6" stroke-linecap="round" stroke-linejoin="round"/>
      </svg>
      <p>If the exchange rate is below your protection rate at expiration, you have no obligation relating to the vanilla call and you are free to buy USD at the cheaper spot rate. If the exchange rate is above your protection rate, your have the right to purchase your USD at the protection rate, and thereby claiming your insurance policy.</p>
    </div>

    <h2 class="section-head">Your bid is not successful:</h2>
    <div class="outcome">
      <svg width="24" height="24" viewBox="0 0 24 24" aria-hidden="true">
        <circle cx="11" cy="13" r="9.5" fill="none" stroke="var(--red)" stroke-width="1.8"/>
        <path d="M6 7l11 12M17 7L6 19" fill="none" stroke="var(--red)" stroke-width="2.6" stroke-linecap="round"/>
      </svg>
      <p>You have no obligation relating to the vanilla option however, if at expiry the exchange rate is above the protection rate, you may exercise your right to buy USD at the lower rate and simultaneous sell USD back at the prevailing spot rate, thereby recouping some or all of the premium paid to buy the option. Alternatively, if you find out your bid was not successful with time still left until expiration, you may sell your option back into the market in the case that it still has residual value, which will depend on various market factors.</p>
    </div>
  </div>

  <svg class="footer" viewBox="0 0 535 70" aria-hidden="true">
    <polygon points="0,33 535,33 535,70 0,70" fill="var(--navy)"/>
    <polygon points="330,33 535,8 535,70 300,70" fill="var(--wedge)"/>
    <polygon points="330,33 535,8 535,5 320,33" fill="var(--teal)"/>
  </svg>
  <div class="footer-label">VANILLA CONTRACTS &nbsp;|&nbsp; 1</div>
</section>

<section class="page page--two">
  <div class="hero" role="img" aria-label="Photo of hands with a pen reviewing printed bar and pie chart reports"></div>

  <div class="features">
    <div class="feature feature--traits">
      <h3>Characteristics</h3>
      <ul>
        <li>You are looking for a straight-forward hedging solution</li>
        <li>You want to receive full benefit from an appreciation of the currency you are exposed to</li>
        <li>You are comfortable receiving protection at the strike rate of the option</li>
        <li>You are willing to pay the non-refundable premium</li>
      </ul>
    </div>
    <div class="feature feature--gains">
      <h3>Advantages</h3>
      <ul>
        <li>You hedge your foreign currency exposure at a predefined hedge rate</li>
        <li>You can choose the hedge rate that suits your budget requirements</li>
        <li>Provides the ability to fully participate in a favourable exchange rate move</li>
        <li>You can choose from most major currency pairs to meet your needs</li>
      </ul>
    </div>
    <div class="feature feature--risks">
      <h3>Risks</h3>
      <ul>
        <li>Premium paid is non-refundable and remains your only obligation when buying vanilla options</li>
      </ul>
    </div>
  </div>

  <div class="content">
    <h2 class="section-head" style="margin-top:0">Why use Vanilla Options?</h2>
    <p>Vanilla options are often compared to an insurance product. The buyer pays a non-refundable premium for the right, but not the obligation to trade currency in the future at the protection rate of the option. This product allows you to participate in a beneficial move to an unlimited extent, which will be the most advantageous outcome, if the exchange rate moves in your favour enough to more than offset the premium paid for the option.</p>

    <h2 class="section-head">What determines the price of a Vanilla Option?</h2>
    <p>The cost of an option is defined by the premium that is required to be paid in order to enter into the contract. Premiums are calculated using the industry standard formulas based upon the Black Scholes model. The most important variables in the option pricing formulas include the following:</p>
    <ul>
      <li>The current market Spot Rate.</li>
      <li>Market volatility – the higher the volatility, the higher the premium.</li>
      <li>The Term of the Option – a longer term typically results in a higher premium.</li>
      <li>The Strike Rate – the closer to being ITM the protection rate is, the higher the premium.</li>
      <li>The interest rate differential of the two currencies involved.</li>
      <li>Style – European or American, or whether the option can be exercised prior to expiration</li>
    </ul>
    <p>An option can either a European (meaning that they can only be exercised on the expiry date), or American (meaning that they can be exercised at any time prior to expiration). We normally deals in European options however, we do offer American options under certain circumstances and when specific delivery terms are agreed upon between us and the customer.</p>
  </div>

  <svg class="footer" viewBox="0 0 535 70" aria-hidden="true">
    <polygon points="0,33 535,33 535,70 0,70" fill="var(--navy)"/>
    <polygon points="330,33 535,8 535,70 300,70" fill="var(--wedge)"/>
    <polygon points="330,33 535,8 535,5 320,33" fill="var(--teal)"/>
  </svg>
  <div class="footer-label">VANILLA CONTRACTS &nbsp;|&nbsp; 2</div>
</section>

</body>
</html>
```